Business Card Design Project

we need a business card design for our company: www.plomvik.ch
It's important to include our already existing logo (see website)

```html
<!DOCTYPE html>
<html lang="en">
<head>
<meta charset="utf-8">
<title>Plomvik business card</title>
<link rel="stylesheet" href="https://fonts.googleapis.com/css2?family=Open+Sans:wght@400;600;700&display=swap">
<style>
  :root {
    --page: #e9ecf0;
    --card: #7aa6d8;
    --stripe: #a8c5e9;
    --stripe-soft: #94b8e2;
    --ink-light: #ffffff;
    --ink-dark: #3b4d66;
    --brand: #1c6ec2;
  }
  * { margin: 0; padding: 0; box-sizing: border-box; }
  html, body {
    width: 848px; height: 1200px; overflow: hidden;
    background: var(--page);
    font-family: "Open Sans", Arial, sans-serif;
  }
  .canvas { position: relative; width: 848px; height: 1200px; }
  .card {
    position: absolute; left: 84px; top: 401px;
    width: 680px; height: 398px;
    background: var(--card);
    box-shadow: 0 6px 18px rgba(40, 60, 90, 0.18);
    overflow: hidden;
  }
  .band { position: absolute; left: 0; width: 100%; }
  .band--top-wide { top: 25px; height: 16px; background: var(--stripe); opacity: .75; }
  .band--top-thin { top: 45px; height: 5px; background: var(--stripe); opacity: .7; }
  .band--bottom-wide { top: 322px; height: 16px; background: var(--stripe); opacity: .75; }
  .band--bottom-thin { top: 344px; height: 5px; background: var(--stripe-soft); }
  .brand {
    position: absolute; left: 56px; top: 60px;
    display: flex; align-items: center; gap: 12px;
  }
  .brand__mark { width: 30px; height: 30px; background: var(--brand); }
  .brand__name {
    font-weight: 700; font-size: 48px; line-height: 1;
    color: var(--ink-light); letter-spacing: -0.5px;
  }
  .brand__url {
    position: absolute; left: 98px; top: 118px;
    font-size: 13px; font-weight: 600; color: var(--brand);
  }
  .holder {
    position: absolute; left: 0; width: 100%; top: 188px;
    padding-left: 100px; text-align: center;
    font-size: 30px; color: var(--ink-light); font-weight: 400;
  }
  .address {
    position: absolute; left: 70px; top: 246px;
    font-style: normal;
    font-size: 15px; line-height: 21px; color: var(--ink-dark);
  }
  .contacts {
    position: absolute; left: 376px; top: 244px;
    list-style: none; font-size: 16px; line-height: 22px; color: var(--ink-dark);
  }
  .contacts li { display: flex; align-items: center; gap: 9px; }
  .contacts svg { width: 16px; height: 14px; flex: none; }
</style>
</head>
<body>
<div class="canvas">
  <section class="card" aria-label="Business card front">
    <div class="band band--top-wide"></div>
    <div class="band band--top-thin"></div>
    <div class="band band--bottom-wide"></div>
    <div class="band band--bottom-thin"></div>

    <div class="brand">
      <span class="brand__mark"></span>
      <span class="brand__name">Plomvik</span>
    </div>
    <div class="brand__url">www.plomvik.ch</div>

    <h1 class="holder">Name Surname</h1>

    <address class="address">
      Lindenweg 12<br>
      3712 Kornau
    </address>

    <ul class="contacts">
      <li>
        <svg viewBox="0 0 16 14" aria-hidden="true"><rect x="1" y="1" width="14" height="9" fill="none" stroke="#3b4d66" stroke-width="1.6"/><rect x="5" y="11" width="6" height="2" fill="#3b4d66"/></svg>
        www.plomvik.ch
      </li>
      <li>
        <svg viewBox="0 0 16 14" aria-hidden="true"><rect x="3" y="1" width="10" height="12" rx="1.5" fill="none" stroke="#3b4d66" stroke-width="1.6"/><rect x="5" y="3" width="6" height="4" fill="#3b4d66"/></svg>
        +41 31 000 12 34
      </li>
      <li>
        <svg viewBox="0 0 16 14" aria-hidden="true"><rect x="1" y="2" width="14" height="10" fill="none" stroke="#3b4d66" stroke-width="1.6"/><path d="M1 2 L8 8 L15 2" fill="none" stroke="#3b4d66" stroke-width="1.6"/></svg>
        info@plomvik.ch
      </li>
    </ul>
  </section>
</div>
</body>
</html>
```